Medical Centre Website

We need a new design for a medical centre based in Perth, Western Australia called 'Tarvin Grove Medical Centre'.

The medical centre does general practitioner work including general checkups, ecg, heart checks, woman's health and more servicing children and adults. They also do home visits on occasions where the patient cannot attend the centre.

They would like an information/brochure website where visitors can read up on the practice, send email and view their location.

The client wish the design to be clean, fresh and light. The main colours are a light purple/blue and to a dark navy blue. The client would not want the logo to be altered in any way. This includes changing the words colours or the image.

The final design should represent a loving, family friendly practice where patients can come to receive the best treatments.

We just need the end product to be presented to un in a layed psd format. The fonts must be as per the W3C standards.

**IMPORTANT**
I have received heaps of chatlink invites in the past. To treat everyone fairly, I do not add people to my chatlink list as in the past people expected us to give them the prize. If you have questions, please ask them in pixel forum as it may benefit others who are also designing the site. If I need to, I will send a message to the user.
Updates

Hi Designers,

Most designs we have received have been overly cluttered. Are you able to simplify the designs.

Cheers, Dorian

Hi Designers,

Some of the designs are quite attractive but aremore cluttered than I would like. If you have a look at the following design, the design is very simple and straight to the point. A lot of designs have too much wording and the reader can be put off. We are looking something more like:

velmoxa.com.au

I would prefer to see designs and have opened up the contest for a further 7 days.

Designers,

We have received feedback from the client and Quite frankly he don’t really like any of them.They are too cluttered and Americanised. All drab blue colours.
 
If you have a look at template monster, these designs are better and cleaner. We do not want heaps of writing on the front page.

If you look at the eariler examples such as quorbeyclinic.com.au which I did myself, the client loves that simplicity of the site.

```html
<!DOCTYPE html>
<html lang="en">
<head>
<meta charset="utf-8">
<title>Tarvin Grove Medical Centre</title>
<link href="https://fonts.googleapis.com/css2?family=Fredoka:wght@600&family=Lato:wght@400;700&display=swap" rel="stylesheet">
<style>
  :root {
    --blue-deep: #1479c4;
    --blue-text: #1a8ccc;
    --sky: #12b4ef;
    --sky-light: #7fd6f7;
    --nav-top: #36b6f2;
    --nav-bottom: #0f8fd8;
    --nav-divider: #0b7cc0;
    --tab-top: #c3d1ef;
    --tab-bottom: #9fb3e2;
    --tab-text: #1e2a4a;
    --violet: #c451c4;
    --violet-dark: #a13aa8;
    --grey-line: #d9dee6;
    --grey-field: #e9eef5;
    --grey-text: #8a93a0;
    --white: #ffffff;
  }
  * { box-sizing: border-box; margin: 0; padding: 0; }
  html, body { width: 1200px; height: 768px; overflow: hidden; background: var(--white); }
  body { position: relative; font-family: "Lato", Arial, sans-serif; }

  .top-tabs {
    position: absolute; left: 565px; top: 6px; width: 462px; height: 39px;
    display: flex; list-style: none;
    background: linear-gradient(var(--tab-top), var(--tab-bottom));
    clip-path: polygon(0 0, 100% 0, 100% 100%, 22px 100%);
  }
  .top-tabs li {
    flex: 1; display: flex; align-items: center; justify-content: center;
    font-size: 13.5px; color: var(--tab-text); border-left: 1px solid #8fa3d4;
  }
  .top-tabs li:first-child { border-left: none; padding-left: 18px; flex: 1.15; }

  .brand {
    position: absolute; left: 121px; top: 52px; display: flex; align-items: center; gap: 14px;
    font-family: "Lato", Arial, sans-serif; font-weight: 400; color: var(--blue-deep);
    font-size: 30px; letter-spacing: 0.5px;
  }
  .brand-mark { width: 40px; height: 40px; border-radius: 50%; background: #a9b9e6; }

  .call {
    position: absolute; right: 173px; top: 58px; display: flex; align-items: center; gap: 6px;
    font-size: 14.5px; color: var(--grey-text); font-weight: 700;
  }
  .call strong { color: var(--blue-deep); }

  .search {
    position: absolute; left: 749px; top: 92px; width: 278px; height: 31px;
    background: var(--grey-field); border: 1px solid var(--grey-line);
    display: flex; align-items: center; justify-content: space-between; padding: 0 9px;
    font-size: 13.5px; color: var(--grey-text);
  }

  .main-nav {
    position: absolute; left: 0; top: 183px; width: 1200px; height: 55px;
    background: linear-gradient(var(--nav-top), var(--nav-bottom));
    border-bottom: 2px solid var(--white);
  }
  .main-nav ul { list-style: none; display: flex; height: 100%; margin-left: 111px; }
  .main-nav li {
    display: flex; align-items: center; padding: 0 16.5px; height: 100%;
    color: var(--white); font-size: 14px; border-right: 1px solid var(--nav-divider);
  }
  .main-nav li:last-child { border-right: none; }

  .hero-sky {
    position: absolute; left: 0; top: 240px; width: 1200px; height: 380px;
    background: radial-gradient(ellipse at 8% 30%, var(--sky-light) 0 18%, transparent 30%),
                radial-gradient(ellipse at 95% 35%, #e9f7fd 0 16%, transparent 26%),
                linear-gradient(var(--sky), #36c0f2 70%, #e8f6fd);
  }

  .hero-card {
    position: absolute; left: 119px; top: 286px; width: 908px; height: 420px;
    background: var(--white); border: 1px solid var(--grey-line);
    box-shadow: 0 1px 4px rgba(0,0,0,0.15);
  }
  .hero-title {
    position: absolute; left: 32px; top: 62px;
    font-family: "Fredoka", "Arial Rounded MT Bold", sans-serif; font-weight: 600;
    font-size: 47px; line-height: 45px; color: var(--blue-text); letter-spacing: -0.5px;
  }
  .hero-title em { font-style: normal; color: var(--violet); }
  .hero-button {
    position: absolute; left: 33px; top: 314px; width: 342px; height: 49px;
    background: linear-gradient(#d56fd6, var(--violet-dark));
    border: 1px solid #8f2f94; color: var(--white);
    font-family: "Fredoka", "Arial Rounded MT Bold", sans-serif; font-weight: 600;
    font-size: 24px; display: flex; align-items: center; justify-content: center;
  }
  .hero-visual {
    position: absolute; left: 465px; top: 80px; width: 420px; height: 255px;
    background: radial-gradient(ellipse at 50% 45%, #e0262c 0 38%, #f4c9ca 52%, var(--white) 70%);
  }

  .slider-dots {
    position: absolute; left: 536px; top: 719px; display: flex; gap: 3px;
  }
  .slider-dots span {
    width: 15px; height: 15px; border-radius: 50%;
    background: #d6d9de; border: 2px solid #a9aeb6;
  }
  .slider-dots span.active { background: #555a62; }
  .slider-dots span.first { background: #9aa0a8; }
</style>
</head>
<body>
  <ul class="top-tabs">
    <li>Appointment</li>
    <li>Find A Doctor</li>
    <li>Locations</li>
    <li>Careers</li>
  </ul>

  <div class="brand"><span class="brand-mark"></span>Tarvin Grove Medical Centre</div>

  <div class="call">
    <svg width="17" height="17" viewBox="0 0 24 24" aria-hidden="true"><path fill="#1a9ad6" d="M6.6 10.8c1.4 2.8 3.8 5.1 6.6 6.6l2.2-2.2c.3-.3.7-.4 1-.2 1.1.4 2.3.6 3.6.6.6 0 1 .4 1 1V20c0 .6-.4 1-1 1C10.6 21 3 13.4 3 4c0-.6.4-1 1-1h3.5c.6 0 1 .4 1 1 0 1.3.2 2.5.6 3.6.1.3 0 .7-.2 1z"/></svg>
    Call US: <strong>555.0187.4420</strong>
  </div>

  <div class="search">
    <span>Search</span>
    <svg width="16" height="16" viewBox="0 0 16 16" aria-hidden="true"><circle cx="9.5" cy="6.5" r="4.5" fill="none" stroke="#1a6fb0" stroke-width="2"/><line x1="6.3" y1="9.7" x2="1.5" y2="14.5" stroke="#1a6fb0" stroke-width="2.4" stroke-linecap="round"/></svg>
  </div>

  <nav class="main-nav">
    <ul>
      <li>HOME</li><li>SERVICES</li><li>LOCATION</li><li>MEET&nbsp; A DOCTOR</li><li>GET A CALL</li><li>CASE HISTORY</li><li>BLOG</li><li>TESTIMONIAL</li><li>CONTACT</li>
    </ul>
  </nav>

  <div class="hero-sky" role="img" aria-label="Bright blue sky with soft white clouds"></div>

  <section class="hero-card">
    <h1 class="hero-title">Did you take care<br>of <em>heart?</em><br>Dont worry we are<br>here to take care of<br>your <em>heart!</em></h1>
    <div class="hero-button">READ THE FULL STORY</div>
    <div class="hero-visual" role="img" aria-label="Red heart with a bandage across a heartbeat line"></div>
  </section>

  <div class="slider-dots"><span class="first"></span><span class="active"></span><span></span><span></span></div>
</body>
</html>
```